Fun relaxed Travel Photography Business Card*

Require a fun, funky and quirky but rememberable business card for a travel photographer

Industry/Entity Type

Photographer

Contact Information for Business Card

Front Card

(my name) Tavo M.

Travel Photographer ( small under travel photographer) “self-proclaimed”

(website logo) wanderingtavo.example

(Instagram logo) @wandering_with_tavo

(Instagram logo) @wandering_with_tavo_2.0 (backup for when Instagram puts Tavo on timeout for bad behaviour)

Tel: N/A (removing the potential awkwardness of me not replying)

Email: (see above)

Back Card

Offending people since 1986

(Bottom right corner) “p.s. travelling made me fatTER”

Font styles to use
Serif

Colors

Designer to choose colors to be used in the design.

Requirements
Must have
• a camera
• a similar cartoon version of me as the "logo" see attached files, try to make as similar as possible

```html
<!DOCTYPE html>
<html lang="en">
<head>
<meta charset="utf-8">
<title>Tavo M. – Travel Photographer Business Card</title>
<link rel="stylesheet" href="https://fonts.googleapis.com/css2?family=Open+Sans:wght@400;600;700&display=swap">
<style>
  :root {
    --page-bg: #e4e2de;
    --card-dark: #1f1d1c;
    --panel-light: #ecebe8;
    --accent-orange: #e8771f;
    --avatar-orange: #f0a024;
    --avatar-deep: #d9801a;
    --ink: #2a2826;
    --tagline: #e9e6e1;
    --footer-text: #d8d5d0;
  }
  * { box-sizing: border-box; margin: 0; padding: 0; }
  html, body {
    width: 1200px; height: 971px; overflow: hidden;
    background: var(--page-bg);
    font-family: "Open Sans", Arial, sans-serif;
  }
  .business-card {
    position: absolute; left: 100px; top: 165px;
    width: 1000px; height: 640px;
    border-radius: 40px;
    background: var(--card-dark);
    overflow: hidden;
    box-shadow: 0 18px 40px rgba(0,0,0,0.18);
  }
  .camera-body { position: absolute; inset: 0; }
  .camera-body path { fill: var(--panel-light); }
  .tagline {
    position: absolute; left: 62px; top: 70px;
    font-size: 34px; font-weight: 600; color: var(--tagline);
    letter-spacing: 0.2px;
  }
  .owner-name {
    position: absolute; left: 100px; top: 232px;
    font-size: 46px; font-weight: 700; color: var(--accent-orange);
    letter-spacing: 0.5px;
  }
  .owner-role {
    position: absolute; left: 102px; top: 296px;
    font-size: 27px; line-height: 33px; color: var(--ink);
  }
  .contact-list {
    position: absolute; left: 100px; top: 410px;
    list-style: none;
  }
  .contact-item {
    display: flex; align-items: center; gap: 10px;
    font-size: 29px; line-height: 40px; color: var(--ink);
  }
  .contact-icon { width: 22px; height: 22px; flex: none; }
  .contact-icon.globe circle, .contact-icon.globe path {
    fill: none; stroke: var(--accent-orange); stroke-width: 2;
  }
  .contact-icon.social-square {
    border: 3px solid var(--accent-orange); border-radius: 4px;
    width: 20px; height: 20px;
  }
  .avatar-portrait {
    position: absolute; left: 590px; top: 160px;
    width: 320px; height: 320px; border-radius: 50%;
    background: radial-gradient(circle at 50% 45%, var(--avatar-orange) 0%, var(--avatar-deep) 100%);
  }
  .signoff {
    position: absolute; right: 60px; bottom: 18px;
    font-size: 27px; color: var(--footer-text);
  }
</style>
</head>
<body>
  <div class="business-card">
    <svg class="camera-body" width="1000" height="640" viewBox="0 0 1000 640" aria-hidden="true">
      <path d="M 90 150 H 150 Q 165 150 170 138 L 178 122 Q 184 110 198 110 H 330 Q 344 110 350 122 L 358 138 Q 363 150 378 150 H 530 Q 545 150 550 135 L 560 85 Q 565 60 590 60 H 830 Q 855 60 860 85 L 866 105 Q 870 120 885 120 H 920 Q 950 120 950 150 V 540 Q 950 570 920 570 H 90 Q 60 570 60 540 V 180 Q 60 150 90 150 Z"/>
    </svg>

    <p class="tagline">Offending people since 1986</p>

    <h1 class="owner-name">TAVO M.</h1>
    <p class="owner-role">Travel Photographer<br>“self-proclaimed”</p>

    <ul class="contact-list">
      <li class="contact-item">
        <svg class="contact-icon globe" viewBox="0 0 22 22" aria-hidden="true">
          <circle cx="11" cy="11" r="9"/>
          <path d="M2 11 H20 M11 2 C6 6 6 16 11 20 M11 2 C16 6 16 16 11 20"/>
        </svg>
        wanderingtavo.example
      </li>
      <li class="contact-item"><span class="contact-icon social-square"></span>@wandering_with_tavo</li>
      <li class="contact-item"><span class="contact-icon social-square"></span>@wandering_with_tavo_2.0</li>
    </ul>

    <div class="avatar-portrait" role="img" aria-label="Cartoon avatar of Tavo in sunglasses and a floral shirt on an orange circle"></div>

    <p class="signoff">“p.s. travelling made me fatTER”</p>
  </div>
</body>
</html>
```